Portfolio site - Need a basic WordPress or SquareSpace site

I need a portfolio site where I have the option to keep updating it on my own. Therefore, I'm guessing I need one that uses WordPress or SquareSpace. I just need a simple and elegant design. I'm a writer (scholarly, fiction and journalism).

Target Market(s)

Adult

Industry/Entity Type

Writer

Number of Pages Required

4 page

Font styles to use
Serif

Colors
b7a5cd
e667a6
85abd2

Requirements
Must have
• Easily updatable features. I'll have to publish links and small blurbs from time to time. And maybe the occasional image.
• Pages should be:
• Home
• Work
• Press
• Contact

```html
<!DOCTYPE html>
<html lang="en">
<head>
<meta charset="utf-8">
<title>Marina Voss — Writer</title>
<link href="https://fonts.googleapis.com/css2?family=Oswald:wght@400;500;600&family=Open+Sans:wght@400;600;700&display=swap" rel="stylesheet">
<style>
:root{
  --pink:#e667a6;
  --lavender:#b7a5cd;
  --blue:#85abd2;
  --ink:#222;
  --text:#555;
  --muted:#888;
  --soft:#f5f5f5;
  --line:#e4e4e4;
  --white:#fff;
}
*{margin:0;padding:0;box-sizing:border-box}
html,body{width:1200px;height:4215px;overflow:hidden;background:var(--white)}
body{font-family:"Open Sans",Arial,sans-serif;color:var(--text);font-size:14px;line-height:1.7}
.page{position:relative;width:1200px;height:4215px;overflow:hidden}
section,header,footer{position:absolute;left:0;width:1200px}
.abs{position:absolute}
.heading{font-family:"Oswald",Arial,sans-serif;color:var(--ink);text-transform:uppercase;letter-spacing:1.5px;font-weight:500}
.center-title{text-align:center;font-size:27px;line-height:1.3}
.center-title::after{content:"";display:block;width:46px;height:3px;background:var(--pink);margin:10px auto 0}
.center-sub{text-align:center;font-size:13px;color:#444;width:560px;left:320px}
.btn{position:absolute;display:flex;align-items:center;justify-content:center;font-family:"Oswald",Arial,sans-serif;color:#fff;text-transform:uppercase;font-size:14px;letter-spacing:1px}
.btn.pink{background:var(--pink)}
.btn.blue{background:var(--blue)}
.btn.dark{background:#2f2f2f}
.btn.ghost{border:1px solid var(--line);color:#333;font-size:12px}

/* Hero */
.hero{top:0;height:632px;background:linear-gradient(100deg,#2a2a2c 0%,#3a3a3d 45%,#4b4a4c 70%,#2b2b2d 100%)}
.hero-photo{position:absolute;left:560px;top:0;width:640px;height:632px;background:radial-gradient(ellipse at 50% 45%,rgba(120,110,105,.55),rgba(40,40,42,0) 70%)}
.logo{left:174px;top:50px;font-family:"Oswald",Arial,sans-serif;font-size:34px;line-height:1.3;color:#fff;letter-spacing:1px;font-weight:400}
.nav{left:634px;top:60px;display:flex;align-items:center}
.nav a{color:#fff;text-decoration:none;font-size:13px;font-weight:600;letter-spacing:.5px;width:96px;text-align:center;position:relative}
.nav a.active::after{content:"";position:absolute;left:32px;right:32px;bottom:-10px;height:2px;background:#fff}
.burger{left:1006px;top:66px}
.hero-kicker{left:174px;top:226px;color:#fff;font-size:15px;line-height:20px;letter-spacing:1px;font-weight:600}
.hero-name{left:174px;top:248px;color:#fff;font-family:"Oswald",Arial,sans-serif;font-size:42px;line-height:52px;font-weight:600;letter-spacing:2px}
.hero-role{left:174px;top:304px;color:#fff;font-size:16px;line-height:22px}
.hero-text{left:174px;top:336px;width:490px;color:#ddd;font-size:14px;line-height:22px}
.arrow{top:292px}
.dots{left:566px;top:582px;display:flex;gap:6px}
.dots i{width:20px;height:5px;background:#ccc;display:block;border-radius:2px}
.dots i:first-child{background:var(--pink)}
.dots i:nth-child(2){background:var(--blue)}

/* About */
.about{top:632px;height:492px}
.about-frame{left:160px;top:59px;width:284px;height:328px;border:2px solid var(--pink)}
.about-photo{left:174px;top:73px;width:292px;height:355px;background:linear-gradient(160deg,#d9d6d3,#a9a3a0 55%,#3b3d4a)}
.about-title{left:528px;top:68px;font-size:30px;line-height:40px}
.about-title span{color:var(--pink)}
.about-role{left:528px;top:110px;font-size:14px;line-height:20px;color:#333;letter-spacing:1px}
.about-text{left:528px;top:142px;width:500px;font-size:13px;line-height:1.75;color:#444}
.contact-line{top:273px;display:flex;align-items:center;gap:10px;font-size:12px;color:#333}
.contact-line b{font-weight:700}
.ring{width:30px;height:30px;border:2px solid var(--pink);border-radius:50%;display:flex;align-items:center;justify-content:center}

/* Experience */
.experience{top:1124px;height:430px;background:var(--soft)}
.exp-photo{left:0;top:0;width:612px;height:430px;background:linear-gradient(120deg,#cbc4c0,#8c8683 60%,#5d5a5c)}
.exp-label{left:318px;top:142px;color:#fff}
.exp-label small{display:block;font-family:"Oswald",Arial,sans-serif;font-size:15px;letter-spacing:1px;line-height:20px}
.exp-label strong{display:block;font-family:"Oswald",Arial,sans-serif;font-size:30px;font-weight:500;letter-spacing:2px;line-height:1.1}
.exp-label p{font-size:12px;width:260px;line-height:1.5;margin-top:8px}
.skill{left:663px;width:362px}
.skill p{font-size:16px;color:#333}
.skill p b{font-weight:700}
.skill .bar{height:3px;background:var(--line);margin-top:10px;position:relative}
.skill .bar i{position:absolute;left:0;top:0;height:3px;display:block}

/* Press */
.press{top:1554px;height:643px}
.press-box{left:441px;top:191px;width:585px;height:391px;background:var(--lavender)}
.press-photo{left:174px;top:228px;width:343px;height:317px;background:linear-gradient(150deg,#eceeea,#b9bcb7 50%,#7e8a6a)}
.press-head{left:540px;top:224px;width:440px;color:#fff;font-family:"Oswald",Arial,sans-serif;font-size:23px;line-height:1.5;letter-spacing:1.5px;text-transform:uppercase;font-weight:500}
.press-text{left:540px;top:312px;width:450px;color:#fff;font-size:12.5px;line-height:1.75}

/* Work */
.work{top:2197px;height:433px;background:var(--soft)}
.work-photo{left:612px;top:0;width:588px;height:433px;background:linear-gradient(120deg,#a9c1db,#7d9ec4 45%,#5d6f86)}
.work-label{left:660px;top:112px;color:#fff}
.feature{width:190px}
.feature h4{font-family:"Oswald",Arial,sans-serif;font-size:13px;color:#222;letter-spacing:.5px;margin-top:8px;font-weight:500}
.feature p{font-size:11.5px;color:#555;line-height:1.45;margin-top:8px}

/* Blog */
.blog{top:2630px;height:643px}
.card{top:217px;width:270px;height:365px;border:1px solid #eee}
.card .thumb{height:180px}
.card .date{font-size:12px;color:#333;margin:12px 16px 0}
.card h3{font-family:"Oswald",Arial,sans-serif;font-size:18px;color:#222;letter-spacing:1px;margin:2px 16px 0;font-weight:500}
.card p{font-size:12.5px;color:#555;margin:6px 16px 0;line-height:1.5}
.card .btn{left:16px;top:312px;width:116px;height:38px}

/* Testimonial */
.testimonial{top:3273px;height:394px;background:linear-gradient(90deg,#c2b2d6,#b7a5cd 50%,#c7b9da)}
.testimonial .center-title{color:#fff}
.testimonial .center-title::after{background:#fff}
.quote-mark{left:580px;top:125px}
.quote{left:340px;top:160px;width:520px;text-align:center;color:#fff;font-size:17px;line-height:1.6}
.quote-name{left:0;width:1200px;top:262px;text-align:center;color:#fff;font-weight:700;font-size:15px}
.quote-role{left:0;width:1200px;top:288px;text-align:center;color:#fff;font-size:12px}
.t-dots{left:586px;top:323px;display:flex;gap:8px}
.t-dots i{width:8px;height:8px;border-radius:50%;background:#fff;display:block}
.t-dots i:last-child{background:var(--pink)}

/* Contact */
.contact{top:3667px;height:463px}
.info{left:174px;display:flex;gap:14px;font-size:12.5px;color:#333;line-height:1.5;align-items:flex-start}
.field{border:1px solid var(--line);font-size:12px;color:#999;padding:8px 10px}

/* Footer */
.footer{top:4130px;height:85px;background:var(--pink)}
.footer p{position:absolute;left:174px;top:33px;color:#fff;font-size:12px}
.social{position:absolute;left:946px;top:36px;display:flex;gap:12px}
.social i{width:12px;height:12px;border-radius:50%;background:#fff;display:block}
</style>
</head>
<body>
<div class="page">

<header class="hero">
  <div class="hero-photo" role="img" aria-label="Photo of a writer working at a laptop, darkened behind the text"></div>
  <div class="abs logo">Marina Voss</div>
  <nav class="abs nav">
    <a class="active" href="#">HOME</a><a href="#">WORK</a><a href="#">PRESS</a><a href="#">CONTACT</a>
  </nav>
  <svg class="abs burger" width="18" height="14" viewBox="0 0 18 14"><rect y="0" width="18" height="2" fill="#fff"/><rect y="6" width="18" height="2" fill="#fff"/><rect y="12" width="18" height="2" fill="#fff"/></svg>
  <svg class="abs arrow" style="left:40px" width="16" height="26" viewBox="0 0 16 26"><path d="M13 2 3 13l10 11" fill="none" stroke="#fff" stroke-width="3"/></svg>
  <svg class="abs arrow" style="left:1138px" width="16" height="26" viewBox="0 0 16 26"><path d="M3 2l10 11L3 24" fill="none" stroke="#fff" stroke-width="3"/></svg>
  <div class="abs hero-kicker">WELCOME! I'M</div>
  <h1 class="abs hero-name">MARINA VOSS</h1>
  <div class="abs hero-role">Writer</div>
  <p class="abs hero-text">The namics of how users interact with interactive elements within a user interface flow chart based on container proportion.</p>
  <div class="btn pink" style="left:174px;top:414px;width:144px;height:40px">My Work</div>
  <div class="btn blue" style="left:331px;top:414px;width:146px;height:40px">Hire Me</div>
  <div class="abs dots"><i></i><i></i><i></i></div>
</header>

<section class="about">
  <div class="abs about-frame"></div>
  <div class="abs about-photo" role="img" aria-label="Portrait photo of the writer at her desk"></div>
  <h2 class="abs heading about-title">About <span>Me</span></h2>
  <div class="abs about-role">WRITER</div>
  <p class="abs about-text">Lorem Ipsum is simply dummy text of the printing and typesetting industry. Lorem Ipsum has been the industry's standard dummy text ever since the 1500s, when an unknown printer took a galley of type and scrambled it to make a type specimen book. It has survived not only five centuries, but also the leap into electronic typesetting, remaining essentially unchanged. of type and.</p>
  <div class="abs contact-line" style="left:528px">
    <span class="ring"><svg width="14" height="14" viewBox="0 0 24 24"><path d="M6.6 10.8a15 15 0 0 0 6.6 6.6l2.2-2.2c.3-.3.7-.4 1-.2 1.1.4 2.3.6 3.6.6.6 0 1 .4 1 1V20c0 .6-.4 1-1 1A17 17 0 0 1 3 4c0-.6.4-1 1-1h3.5c.6 0 1 .4 1 1 0 1.3.2 2.5.6 3.6.1.3 0 .7-.2 1z" fill="var(--pink)"/></svg></span>
    <span><b>Phone:</b> +10 555 014 22 80</span>
  </div>
  <div class="abs contact-line" style="left:746px">
    <span class="ring"><svg width="14" height="14" viewBox="0 0 24 24"><path d="M6.6 10.8a15 15 0 0 0 6.6 6.6l2.2-2.2c.3-.3.7-.4 1-.2 1.1.4 2.3.6 3.6.6.6 0 1 .4 1 1V20c0 .6-.4 1-1 1A17 17 0 0 1 3 4c0-.6.4-1 1-1h3.5c.6 0 1 .4 1 1 0 1.3.2 2.5.6 3.6.1.3 0 .7-.2 1z" fill="var(--pink)"/></svg></span>
    <span><b>Phone:</b> hello@marinavoss.com</span>
  </div>
  <div class="btn pink" style="left:528px;top:346px;width:134px;height:37px;font-size:12px">Download CV</div>
  <div class="btn blue" style="left:675px;top:346px;width:134px;height:37px;font-size:12px">Send Message</div>
</section>

<section class="experience">
  <div class="abs exp-photo" role="img" aria-label="Photo of the writer typing at a laptop"></div>
  <svg class="abs" style="left:0;top:0" width="612" height="430" viewBox="0 0 612 430"><polygon points="260,0 612,0 612,430 210,430 290,230" fill="var(--pink)" opacity=".85"/></svg>
  <div class="abs exp-label">
    <small>WORK</small><strong>EXPERIENCE</strong>
    <p>The vetrics of how users interact with interactive elements within a user interface.</p>
  </div>
  <div class="abs skill" style="top:118px"><p><b>Scholarly</b> - 5 years of experience</p><div class="bar"><i style="width:90%;background:var(--lavender)"></i></div></div>
  <div class="abs skill" style="top:177px"><p><b>Fiction</b> - 3 years of experience</p><div class="bar"><i style="width:55%;background:var(--pink)"></i></div></div>
  <div class="abs skill" style="top:244px"><p><b>Journalism</b> - 2 years of experience</p><div class="bar"><i style="width:40%;background:var(--blue)"></i></div></div>
</section>

<section class="press">
  <h2 class="abs heading center-title" style="left:0;width:1200px;top:52px">Press</h2>
  <p class="abs center-sub" style="top:122px">The namics of how users interact with interactive elements within a user interface flow chart based on container proportion.</p>
  <div class="abs press-box"></div>
  <div class="abs press-photo" role="img" aria-label="Photo of an open magazine with fanned pages"></div>
  <h3 class="abs press-head">Lorem ipsum is simply dummy text of the printing lorem ipsum is</h3>
  <p class="abs press-text">Lorem Ipsum is simply dummy text of the printing and typesetting industry. Lorem Ipsum has been the industry's standard dummy text ever since the 1500s, when an unknown printer took a galley of type and scrambled it to make a type specimen book. It has survived not only five centuries, but also the leap into electronic typesetting, and scrambled it to make a type specimen book. It has survived not only five centuries, but also the leap into electronic typesetting, remaining essentially unchanged.</p>
  <div class="btn dark" style="left:540px;top:508px;width:134px;height:38px;font-size:12px">Read More</div>
</section>

<section class="work">
  <div class="abs feature" style="left:171px;top:60px">
    <svg width="40" height="34" viewBox="0 0 40 34"><path d="M20 3 37 11 20 19 3 11z M3 17l17 8 17-8 M3 23l17 8 17-8" fill="none" stroke="#555" stroke-width="1.5"/></svg>
    <h4>LOREM IPSUM IS SIMPLY</h4><p>It is a long established fact that a reader will be distracted by the readable content of a</p>
  </div>
  <div class="abs feature" style="left:391px;top:60px">
    <svg width="46" height="34" viewBox="0 0 46 34"><circle cx="14" cy="20" r="9" fill="none" stroke="#555" stroke-width="1.5" stroke-dasharray="4 2"/><circle cx="14" cy="20" r="4" fill="none" stroke="#555" stroke-width="1.5"/><circle cx="32" cy="10" r="7" fill="none" stroke="#555" stroke-width="1.5" stroke-dasharray="3 2"/><circle cx="32" cy="10" r="3" fill="none" stroke="#555" stroke-width="1.5"/></svg>
    <h4>LOREM IPSUM IS SIMPLY</h4><p>It is a long established fact that a reader will be distracted by the readable content of a</p>
  </div>
  <div class="abs feature" style="left:171px;top:222px">
    <svg width="40" height="34" viewBox="0 0 40 34"><path d="M6 30 30 6l4 4-24 24H6z M4 4l30 26" fill="none" stroke="#555" stroke-width="1.5"/></svg>
    <h4>LOREM IPSUM IS SIMPLY</h4><p>It is a long established fact that a reader will be distracted by the readable content of a</p>
  </div>
  <div class="abs feature" style="left:391px;top:222px">
    <svg width="40" height="34" viewBox="0 0 40 34"><path d="M20 2a10 10 0 0 0-6 18v5h12v-5a10 10 0 0 0-6-18z M15 29h10 M17 32h6" fill="none" stroke="#555" stroke-width="1.5"/></svg>
    <h4>LOREM IPSUM IS SIMPLY</h4><p>It is a long established fact that a reader will be distracted by the readable content of a</p>
  </div>
  <div class="abs work-photo" role="img" aria-label="Photo of hands working on a laptop"></div>
  <svg class="abs" style="left:612px;top:0" width="588" height="433" viewBox="0 0 588 433"><polygon points="0,0 260,0 340,230 300,433 0,433" fill="var(--blue)" opacity=".8"/></svg>
  <div class="abs exp-label work-label">
    <small>MY</small><strong>WORK</strong>
    <p>The vetrics of how users interact with interactive elements within a user interface.</p>
  </div>
</section>

<section class="blog">
  <h2 class="abs heading center-title" style="left:0;width:1200px;top:50px">Recent Blog</h2>
  <p class="abs center-sub" style="top:118px">Lorem Ipsum is simply dummy text of the printing and typesetting industry. Lorem Ipsum has been the industry's standard dummy text ever since the 1500s.</p>
  <article class="abs card" style="left:174px">
    <div class="thumb" role="img" aria-label="Photo of a laptop with printed charts" style="background:linear-gradient(140deg,#e2b57a,#a3794d 60%,#5a4a3c)"></div>
    <div class="date">23 JULY, 2018</div><h3>LOREM IPSUM IS SIMPLY</h3>
    <p>Lorem Ipsum is simply dummy text of the printing and typesetting industry. Lorem Ipsum has been the industry's.</p>
    <div class="btn ghost">READ MORE</div>
  </article>
  <article class="abs card" style="left:466px">
    <div class="thumb" role="img" aria-label="Photo of an open magazine" style="background:linear-gradient(150deg,#eceeea,#b9bcb7 50%,#7e8a6a)"></div>
    <div class="date">20 JULY, 2018</div><h3>LOREM IPSUM IS SIMPLY</h3>
    <p>Lorem Ipsum is simply dummy text of the printing and typesetting industry. Lorem Ipsum has been the industry's.</p>
    <div class="btn ghost">READ MORE</div>
  </article>
  <article class="abs card" style="left:759px">
    <div class="thumb" role="img" aria-label="Photo of a person typing on a laptop" style="background:linear-gradient(140deg,#dfe3e8,#aab3bd 55%,#6f7a86)"></div>
    <div class="date">21 JULY, 2018</div><h3>LOREM IPSUM IS SIMPLY</h3>
    <p>Lorem Ipsum is simply dummy text of the printing and typesetting industry. Lorem Ipsum has been the industry's.</p>
    <div class="btn ghost">READ MORE</div>
  </article>
</section>

<section class="testimonial" role="img" aria-label="Faint photo of a workspace behind a lavender tint">
  <h2 class="abs heading center-title" style="left:0;width:1200px;top:48px">Testimonial</h2>
  <svg class="abs quote-mark" width="40" height="24" viewBox="0 0 40 24"><path d="M4 22c0-9 4-15 12-18v4c-4 2-6 5-6 8h6v6z M22 22c0-9 4-15 12-18v4c-4 2-6 5-6 8h6v6z" fill="#fff"/></svg>
  <p class="abs quote">Lorem Ipsum is simply dummy text of the printing and typesetting industry. Lorem Ipsum has been the industry's standard dummy text ever since the 1500s</p>
  <div class="abs quote-name">Dana Hollis</div>
  <div class="abs quote-role">Lorem Ipsum is simply dummy</div>
  <div class="abs t-dots"><i></i><i></i></div>
</section>

<section class="contact">
  <h2 class="abs heading center-title" style="left:0;width:1200px;top:56px">Contact Us</h2>
  <p class="abs center-sub" style="top:122px">The namics of how users interact with interactive elements within a user interface flow chart based on container proportion.</p>
  <div class="abs info" style="top:223px">
    <svg width="14" height="18" viewBox="0 0 14 18"><path d="M7 0a7 7 0 0 0-7 7c0 5 7 11 7 11s7-6 7-11a7 7 0 0 0-7-7zm0 10a3 3 0 1 1 0-6 3 3 0 0 1 0 6z" fill="#222"/></svg>
    <span>Studio 4, Elm Row, Harbor Point<br>NY, 1208</span>
  </div>
  <div class="abs info" style="top:282px">
    <svg width="14" height="14" viewBox="0 0 24 24"><path d="M6.6 10.8a15 15 0 0 0 6.6 6.6l2.2-2.2c.3-.3.7-.4 1-.2 1.1.4 2.3.6 3.6.6.6 0 1 .4 1 1V20c0 .6-.4 1-1 1A17 17 0 0 1 3 4c0-.6.4-1 1-1h3.5c.6 0 1 .4 1 1 0 1.3.2 2.5.6 3.6.1.3 0 .7-.2 1z" fill="#222"/></svg>
    <span>Phone: +10 555 014 22 80</span>
  </div>
  <div class="abs info" style="top:320px">
    <svg width="16" height="12" viewBox="0 0 16 12"><rect width="16" height="12" fill="#222"/><path d="M0 0l8 7 8-7" fill="none" stroke="#fff" stroke-width="1.2"/></svg>
    <span>Mail: hello@marinavoss.com</span>
  </div>
  <div class="abs field" style="left:540px;top:216px;width:239px;height:36px">Name...</div>
  <div class="abs field" style="left:787px;top:216px;width:239px;height:36px">Message...</div>
  <div class="abs field" style="left:540px;top:264px;width:486px;height:70px">Message...</div>
  <div class="btn pink" style="left:540px;top:357px;width:124px;height:35px;font-size:12px">Submit</div>
</section>

<footer class="footer">
  <p>©2018 Portfolio Site. All Right Reserved.</p>
  <div class="social"><i></i><i></i><i></i><i></i></div>
</footer>

</div>
</body>
</html>
```